DEAN COLLOPY PROPERTY SERVICES

I want a business card that is clean and simple.
'Dean Collopy Property Services' is the title.
Somewhere on the card needs to be 'Carpentry, Tiling, painting and garden services'

On the back of card
PH 087 394 1526
email: deancollopypropertyservices@fernmail.net

I have attached a picture of my other business. I would like the font and design to be similar to the bathroom business.

Many thanks.

```html
<!DOCTYPE html>
<html lang="en">
<head>
<meta charset="utf-8">
<title>Dean Collopy Property Services – Business Card</title>
<link rel="stylesheet" href="https://fonts.googleapis.com/css2?family=Lato:wght@300;400;700&display=swap">
<style>
  :root {
    --backdrop: #2a2a2c;
    --card: #1b1c1e;
    --card-tone: #222325;
    --ink: #ffffff;
    --ink-soft: #d6d6d6;
    --ink-muted: #a9a9a9;
    --rule: #4a4b4e;
  }
  * { box-sizing: border-box; margin: 0; padding: 0; }
  html, body {
    width: 1200px;
    height: 1108px;
    overflow: hidden;
    background: var(--backdrop);
    font-family: "Lato", sans-serif;
  }
  .sheet {
    position: relative;
    width: 1200px;
    height: 1108px;
    display: flex;
    justify-content: center;
    align-items: center;
    gap: 60px;
  }
  .card {
    width: 460px;
    height: 700px;
    border-radius: 26px;
    background: var(--card);
    box-shadow: 0 18px 40px rgba(0,0,0,0.45);
    position: relative;
    overflow: hidden;
  }

  /* Front */
  .card--front {
    display: flex;
    flex-direction: column;
    align-items: center;
    text-align: center;
    color: var(--ink);
    padding: 120px 30px 0;
  }
  .brand {
    display: flex;
    flex-direction: column;
    align-items: center;
  }
  .brand__name {
    font-size: 52px;
    font-weight: 400;
    letter-spacing: -0.5px;
    line-height: 1;
  }
  .brand__tagline {
    margin-top: 12px;
    font-size: 17px;
    font-weight: 400;
    letter-spacing: 5px;
    color: var(--ink);
  }
  .person {
    margin-top: 150px;
  }
  .person__name {
    font-size: 27px;
    font-weight: 700;
    letter-spacing: 0.5px;
  }
  .person__role {
    font-size: 19px;
    font-weight: 400;
    margin-top: 2px;
  }
  .divider {
    width: 110px;
    height: 1px;
    background: var(--rule);
    margin: 18px 0;
  }
  .contact {
    font-size: 20px;
    font-weight: 400;
    line-height: 1.35;
    color: var(--ink);
  }
  .services {
    font-size: 22px;
    font-weight: 300;
    line-height: 1.3;
    letter-spacing: 0.5px;
    color: var(--ink-muted);
  }

  /* Back */
  .card--back {
    background: var(--card);
  }
  .back__texture {
    position: absolute;
    inset: 0;
    background: linear-gradient(160deg, var(--card-tone) 0%, var(--card) 55%, var(--card-tone) 100%);
  }
  .back__mark {
    position: absolute;
    left: 0;
    right: 0;
    top: 420px;
    text-align: center;
    color: var(--ink);
    font-size: 44px;
    font-weight: 400;
    letter-spacing: -0.3px;
  }
</style>
</head>
<body>
  <main class="sheet">
    <section class="card card--front" aria-label="Card front">
      <div class="brand">
        <span class="brand__name">Dean Collopy</span>
        <span class="brand__tagline">PROPERTY SERVICES</span>
      </div>
      <div class="person">
        <p class="person__name">LIAM BRENNAN</p>
        <p class="person__role">Managing Director</p>
      </div>
      <div class="divider"></div>
      <div class="contact">
        <p>087 394 1526</p>
        <p>deancollopypropertyservices@fernmail.net</p>
      </div>
      <div class="divider"></div>
      <div class="services">
        <p>CARPENTRY • TILING</p>
        <p>PAINTING • GARDEN SERVICES</p>
      </div>
    </section>

    <section class="card card--back" aria-label="Card back">
      <div class="back__texture" role="img" aria-label="Tone-on-tone repeated brand name pattern in spot gloss"></div>
      <p class="back__mark">Dean Collopy</p>
    </section>
  </main>
</body>
</html>
```